Tozvar new design for business cards we want to change our existing design. Logo must remain the same

Hello we are the company TozVar and offer various services regarding transportation and disposal. In addition to our main acquisition of van rental, we also offer disposal and express transportation, so we need new business card designs for our business. Our elders have their time and do not like it anymore. We want to change our existing design. Logo must remain the same as well as the color blue, whether dark or light Does not play a big role in the best medium blue. Logo must be present on the front side. As well as telephone, email, web and location. Big enough but not too big. Back can be redesigned Logo as well as name TozVar must be present. Important is the text: Van rental Disposal and clearing express transportation. Without bail in red should be noted somewhere. it should be modern but not too playful. rather serious but no beating company Thank you very much

Target Market(s)

Private customers as well as companies we want to change our existing design. Logo must remain the same as well as the color blue, whether dark or light Does not play a big role in the best medium blue. Logo must be present on the front side. As well as telephone, email, web and location. Big enough but not too big. Back can be redesigned Logo as well as name TozVar must be present. Important is the text: Van rental Disposal and clearing express transportation. Without bail in red should be noted somewhere. it should be modern but not too playful. rather serious but no beating company Thank you very much

Industry/Entity Type

Car Rental

Contact Information for Business Card

we want to change our existing design. Logo must remain the same as well as the color blue, whether dark or light Does not play a big role in the best medium blue.
Logo must be present on the front side.
As well as telephone, email, web and location. Big enough but not too big.
Back can be redesigned Logo as well as name TozVar must be present.
Important is the text:
Van rental
Disposal and clearing
Express transportation.
Without bail in red should be noted somewhere.
it should be modern but not too playful. rather serious but no beating company
Thank you very much

Font styles to use
Sans Serif

Colors
33a6d7
ec1f27
0692cd
3277b5

Requirements
Must have
• logo and name TozVar as described in the above text must have it. we want to change our existing design. Logo must remain the same as well as the color blue, whether dark or light Does not play a big role in the best medium blue. Logo must be present on the front side. As well as telephone, email, web and location. Big enough but not too big. Back can be redesigned Logo as well as name TozVar must be present. Important is the text: Van rental Disposal and clearing express transportation. Without bail in red should be noted somewhere. it should be modern but not too playful. rather serious but no beating company Thank you very much
Nice to have
• see description we want to change our existing design. Logo must remain the same as well as the color blue, whether dark or light Does not play a big role in the best medium blue. Logo must be present on the front side. As well as telephone, email, web and location. Big enough but not too big. Back can be redesigned Logo as well as name TozVar must be present. Important is the text: Van rental Disposal and clearing express transportation. Without bail in red should be noted somewhere. it should be modern but not too playful. rather serious but no beating company Thank you very much
Should not have
• Blue White and little red we want to change our existing design. Logo must remain the same as well as the color blue, whether dark or light Does not play a big role in the best medium blue. Logo must be present on the front side. As well as telephone, email, web and location. Big enough but not too big. Back can be redesigned Logo as well as name TozVar must be present. Important is the text: Van rental Disposal and clearing express transportation. Without bail in red should be noted somewhere. it should be modern but not too playful. rather serious but no beating company Thank you very much

```html
<!DOCTYPE html>
<html lang="de">
<head>
<meta charset="utf-8">
<title>TozVar GmbH – Visitenkarten</title>
<link rel="stylesheet" href="https://fonts.googleapis.com/css2?family=Montserrat:wght@300;400;600;700&family=Oswald:wght@600&display=swap">
<style>
  :root {
    --navy: #33336b;
    --mid-blue: #56698f;
    --light-blue: #7d93ab;
    --paper: #f3f3f5;
    --backdrop: #e8e8ea;
    --contact-text: #e6e7f0;
  }
  * { box-sizing: border-box; margin: 0; padding: 0; }
  html, body { width: 1200px; height: 1138px; overflow: hidden; }
  body { background: var(--backdrop); position: relative; font-family: "Montserrat", sans-serif; }

  .card {
    position: absolute;
    left: 220px;
    width: 760px;
    height: 492px;
    background: var(--paper);
    overflow: hidden;
    box-shadow: 0 6px 22px rgba(0,0,0,0.12);
  }
  .card--contact { top: 40px; }
  .card--services { top: 606px; }
  .card__shapes { position: absolute; inset: 0; width: 100%; height: 100%; }

  .wordmark {
    position: absolute;
    display: flex;
    align-items: center;
    gap: 14px;
    color: var(--navy);
    font-family: "Montserrat", sans-serif;
    font-weight: 700;
    letter-spacing: 4px;
  }
  .wordmark__square { width: 42px; height: 42px; background: var(--navy); }
  .card--contact .wordmark { left: 420px; top: 300px; font-size: 50px; }
  .card--services .wordmark { left: 60px; top: 48px; font-size: 46px; }

  .contact-list { position: absolute; left: 58px; top: 62px; list-style: none; }
  .contact-list__item {
    display: flex; align-items: flex-start; gap: 22px;
    color: var(--contact-text); font-weight: 300; font-size: 24px; line-height: 1.25;
    margin-bottom: 22px;
  }
  .contact-list__icon {
    flex: none; width: 44px; height: 44px; border-radius: 50%;
    border: 2px solid var(--light-blue);
    display: flex; align-items: center; justify-content: center;
  }
  .contact-list__icon svg { width: 20px; height: 20px; }

  .services { position: absolute; left: 72px; top: 140px; list-style: none; }
  .services__item {
    font-family: "Oswald", sans-serif; font-weight: 600; text-transform: uppercase;
    color: var(--navy); font-size: 33px; line-height: 1.22; letter-spacing: 0.5px;
  }
  .services__item::before { content: "• "; }

  .web-line {
    position: absolute; right: 0; bottom: 60px;
    display: flex; align-items: center; gap: 16px;
    color: #fff; font-weight: 700; font-size: 24px; letter-spacing: 1px;
  }
  .web-line__rule { width: 90px; height: 2px; background: #fff; }
</style>
</head>
<body>

  <section class="card card--contact" aria-label="Kontaktseite">
    <svg class="card__shapes" viewBox="0 0 760 492" preserveAspectRatio="none" aria-hidden="true">
      <rect width="760" height="492" fill="var(--navy)"/>
      <path d="M470 0 C420 200 360 360 280 492 L760 492 L760 0 Z" fill="var(--mid-blue)"/>
      <path d="M600 0 C500 150 400 300 320 492 L760 492 L760 0 Z" fill="var(--light-blue)"/>
      <path d="M760 120 C560 140 400 280 350 492 L760 492 Z" fill="var(--paper)"/>
    </svg>

    <ul class="contact-list">
      <li class="contact-list__item">
        <span class="contact-list__icon"><svg viewBox="0 0 24 24" fill="none" stroke="var(--light-blue)" stroke-width="2"><path d="M5 3h4l2 5-3 2a12 12 0 0 0 6 6l2-3 5 2v4a2 2 0 0 1-2 2A17 17 0 0 1 3 5a2 2 0 0 1 2-2z"/></svg></span>
        <span>+41 71 555 20 40</span>
      </li>
      <li class="contact-list__item">
        <span class="contact-list__icon"><svg viewBox="0 0 24 24" fill="var(--light-blue)"><path d="M2 11 22 3l-8 19-3-8z"/></svg></span>
        <span>info@tozvar.ch</span>
      </li>
      <li class="contact-list__item">
        <span class="contact-list__icon"><svg viewBox="0 0 24 24" fill="none" stroke="var(--light-blue)" stroke-width="2"><path d="M12 22s7-7 7-12a7 7 0 0 0-14 0c0 5 7 12 7 12z"/><circle cx="12" cy="10" r="2.5"/></svg></span>
        <span>Lindenweg 14<br>8500 Frauenfeld</span>
      </li>
      <li class="contact-list__item">
        <span class="contact-list__icon"><svg viewBox="0 0 24 24" fill="var(--light-blue)"><circle cx="12" cy="5" r="3"/><circle cx="5" cy="18" r="3"/><circle cx="19" cy="18" r="3"/><path d="M12 5 5 18h14z" fill="none" stroke="var(--light-blue)" stroke-width="1.5"/></svg></span>
        <span>www.tozvar.ch</span>
      </li>
    </ul>

    <div class="wordmark"><span class="wordmark__square"></span>TOZVAR</div>
  </section>

  <section class="card card--services" aria-label="Leistungsseite">
    <svg class="card__shapes" viewBox="0 0 760 492" preserveAspectRatio="none" aria-hidden="true">
      <rect width="760" height="492" fill="var(--paper)"/>
      <path d="M520 0 C640 120 520 360 300 492 L760 492 L760 0 Z" fill="var(--light-blue)"/>
      <path d="M640 0 C700 140 560 380 320 492 L760 492 L760 0 Z" fill="var(--mid-blue)"/>
      <path d="M760 110 C640 200 560 400 340 492 L760 492 Z" fill="var(--navy)"/>
    </svg>

    <div class="wordmark"><span class="wordmark__square"></span>TOZVAR</div>

    <ul class="services">
      <li class="services__item">Transporter Vermietung</li>
      <li class="services__item">Entsorgung und Entrümpelung</li>
      <li class="services__item">Express Transportation</li>
    </ul>

    <div class="web-line"><span>www.TozVar.ch</span><span class="web-line__rule"></span></div>
  </section>

</body>
</html>
```